Etiketten Tüte Lakritz Retro
Zielgruppe
Unter unserer Marke 'GabenZauberei' vertreiben wir Geschenkkombinationen. Z.B. In einem Karton befindet sich eine Flasche Wein, eine Pestosauce und eine Packung Nudeln. Das ganze heißt dann z.B. 'Italienischer Abend'.
Nun möchten wir starten mit einer neuen Reihe. Dabei handelt es sich um Tüten, wie man Sie vom Jahrmarkt kennt. Mit diesen Tüten bedient man sich am Stand einzelner Süßigkeiten. Diese werden abgewogen und bezahlt. Oder man kennt es von früher aus der Kindheit im kleinen Einkaufsladen im Dorf in dem man sich nach der Schule ein Tüte für wenige Pfennig zusammenstellen konnte.
Also wir werden druchsichtige Plastik-Tüten anbieten, die mit Lakritz befüllt sind. Auf die Tüte muss ein Etikett.
Aufgabenstellung
Inhalt der Tüte ist hochwertiges Lakritz aus Schweden.
Wir möchten gerne folgende Message/Gefühl transportieren:
- hochwertiges Lakritz aus Schweden. Qualität.
- Retro. Die gute alte Zeit. Eben Nicht jung, trendy, fresch. Eben so als hätte man sich die Tüte im Tante-Emma-Laden gekauft.
- Das Logo von GabenZauberei muss auf das Etikett

```html
<!DOCTYPE html>
<html lang="de">
<head>
<meta charset="utf-8">
<title>Lakritz – Etikett</title>
<link rel="stylesheet" href="https://fonts.googleapis.com/css2?family=Federant&family=Didact+Gothic&display=swap">
<style>
  :root {
    --paper: #f2e4c7;
    --paper-edge: #e9d6b2;
    --licorice-red: #d4603f;
    --brown: #5a3b22;
    --frame-green: #3f7a4e;
    --pale-green: #c9dcc1;
    --ink: #2a2a2a;
    --ornament-soft: #c7a57c;
  }
  * { margin: 0; padding: 0; box-sizing: border-box; }
  html, body { width: 1200px; height: 897px; overflow: hidden; background: var(--paper); }
  .label {
    position: relative; width: 1200px; height: 897px;
    background: radial-gradient(ellipse at center, var(--paper) 60%, var(--paper-edge) 100%);
    color: var(--brown);
  }
  .frame-lines { position: absolute; inset: 0; }
  .ornament {
    position: absolute; border-radius: 40px;
    background: radial-gradient(circle at center, rgba(212,96,63,.45), rgba(90,59,34,.35) 70%, rgba(90,59,34,0) 100%);
  }
  .ornament.corner-tl { left: 40px; top: 40px; width: 250px; height: 165px; }
  .ornament.corner-tr { right: 40px; top: 40px; width: 250px; height: 165px; }
  .ornament.corner-bl { left: 40px; bottom: 40px; width: 250px; height: 165px; }
  .ornament.corner-br { right: 40px; bottom: 40px; width: 250px; height: 165px; }
  .ornament.top-center { left: 505px; top: 58px; width: 190px; height: 42px; border-radius: 20px; }
  .ornament.bottom-center { left: 505px; bottom: 58px; width: 190px; height: 42px; border-radius: 20px; }
  .ornament.flourish {
    background: linear-gradient(90deg, rgba(90,59,34,0), rgba(90,59,34,.35), rgba(90,59,34,0));
    border-radius: 50%;
  }
  .ornament.flourish-left { left: 167px; top: 398px; width: 162px; height: 105px; }
  .ornament.flourish-right { left: 874px; top: 398px; width: 162px; height: 105px; }
  .ornament.swirl-date { left: 183px; top: 594px; width: 73px; height: 91px; border-radius: 50%; }
  .ornament.swirl-logo { left: 409px; top: 597px; width: 67px; height: 95px; border-radius: 50%; }
  .ribbon {
    position: absolute; left: 821px; top: 605px; width: 213px; height: 135px;
    background: linear-gradient(160deg, var(--pale-green), var(--frame-green));
    clip-path: polygon(0 70%, 78% 0, 100% 20%, 30% 100%);
    opacity: .8;
  }
  .title {
    position: absolute; left: 0; right: 0; top: 196px;
    text-align: center; font-family: "Federant", serif;
    font-size: 176px; line-height: 1; color: var(--licorice-red); letter-spacing: 2px;
  }
  .subtitle {
    position: absolute; left: 0; right: 0; top: 376px;
    text-align: center; font-family: "Federant", serif;
    font-size: 23px; color: var(--brown); letter-spacing: .5px;
  }
  .description {
    position: absolute; left: 0; right: 0; top: 450px;
    text-align: center; font-family: "Didact Gothic", sans-serif;
    font-size: 14.5px; line-height: 20px; color: var(--ink);
  }
  .brand-inline { font-family: "Didact Gothic", sans-serif; color: var(--ink); }
  .date {
    position: absolute; left: 243px; top: 646px; width: 153px;
    text-align: center; font-family: "Didact Gothic", sans-serif;
    font-size: 20px; color: var(--brown);
    border-bottom: 1.5px solid var(--brown); padding-bottom: 6px;
  }
  .brand-mark {
    position: absolute; left: 440px; top: 649px; width: 248px;
    text-align: center; font-family: "Didact Gothic", sans-serif;
    font-size: 22px; color: var(--brown);
    border-bottom: 1.5px solid var(--brown); padding-bottom: 6px;
  }
  .weight-seal {
    position: absolute; left: 720px; top: 611px; width: 128px; height: 128px; border-radius: 50%;
    background: var(--licorice-red); border: 7px solid var(--frame-green);
    box-shadow: 0 0 0 3px var(--paper), 0 0 0 5px var(--frame-green);
    display: flex; align-items: center; justify-content: center;
    font-family: "Didact Gothic", sans-serif; font-size: 22px; color: var(--brown);
    padding-top: 30px;
  }
</style>
</head>
<body>
<main class="label">
  <svg class="frame-lines" width="1200" height="897" viewBox="0 0 1200 897" aria-hidden="true">
    <rect x="11" y="13" width="1178" height="871" fill="none" stroke="#2a2a2a" stroke-width="1.2"/>
    <rect x="56" y="56" width="1088" height="785" fill="none" stroke="var(--frame-green)" stroke-width="3"/>
    <rect x="64" y="64" width="1072" height="769" fill="none" stroke="var(--frame-green)" stroke-width="1.5"/>
    <rect x="76" y="76" width="1048" height="745" fill="none" stroke="var(--frame-green)" stroke-width="4" stroke-dasharray="2 3"/>
    <rect x="86" y="86" width="1028" height="725" fill="none" stroke="var(--frame-green)" stroke-width="1.5"/>
  </svg>

  <div class="ornament corner-tl" role="img" aria-label="Jugendstil-Eckornament mit Ranken und Fächern"></div>
  <div class="ornament corner-tr" role="img" aria-label="Jugendstil-Eckornament mit Ranken und Fächern"></div>
  <div class="ornament corner-bl" role="img" aria-label="Jugendstil-Eckornament mit Ranken und Fächern"></div>
  <div class="ornament corner-br" role="img" aria-label="Jugendstil-Eckornament mit Ranken und Fächern"></div>
  <div class="ornament top-center" role="img" aria-label="Rankenornament oben mittig"></div>
  <div class="ornament bottom-center" role="img" aria-label="Rankenornament unten mittig"></div>

  <h1 class="title">Lakritz</h1>
  <p class="subtitle">hochwertiges Lakritz aus Schweden</p>
  <div class="ornament flourish flourish-left" role="img" aria-label="Verschnörkelte Zierlinie links"></div>
  <div class="ornament flourish flourish-right" role="img" aria-label="Verschnörkelte Zierlinie rechts"></div>

  <p class="description">
    Für all unsere leckeren Lakritzprodukte verwenden wir nur<br>
    hochwertige Süßholzsäfte ausgewählter Lieferanten.<br>
    So wissen wir, dass Geschmack und Aussehen von<br>
    <span class="brand-inline">GabenZauberei</span> Lakritz immer unseren Qualitätsansprüchen entsprechen.
  </p>

  <div class="ornament swirl-date" role="img" aria-label="Spiralförmiger Schnörkel"></div>
  <p class="date">2018/10/22</p>
  <div class="ornament swirl-logo" role="img" aria-label="Spiralförmiger Schnörkel"></div>
  <p class="brand-mark">GabenZauberei®</p>

  <div class="ribbon" role="img" aria-label="Grünes Zierband mit Markenname"></div>
  <div class="weight-seal">300g</div>
</main>
</body>
</html>
```